Business Card Design For Office Furniture Clearance Company

Kestrel Office Clearance - our company name pretty much explains what we do, we clear offices for high end clients, mainly plc's and large international companies.

We require a nice looking business card that displays professionalism but without being too serious.

It would be nice to see just a little more than a conventional boring business card, make sure you add some flare.

Industry/Entity Type

Office Furniture

Contact Information for Business Card

CARD 1

Mark Holloway
Director
mark@kestrelofficeclear.co.uk
m: 07700 913528

t: 01632 960418
www.kestrelofficeclear.co.uk

Kestrel Office Clearance
Unit K4 B
3-7 Fenwick Lane
Ashcombe
Marlow Vale
ZX9 4QT

free office clearances… you cant get better than that.

CARD 2

Peter Donaldson
Director
peter@kestrelofficeclear.co.uk
m: 07700 927153

t: 01632 960418

Kestrel Office Clearance
Unit K4 B
3-7 Fenwick Lane
Ashcombe
Marlow Vale
ZX9 4QT

Font styles to use
Sans Serif

Requirements
Must have
• A white background - as we have a blue logo.
Nice to have
• Nice use of the logo - play around with this and dissect it.

```html
<!DOCTYPE html>
<html lang="en">
<head>
<meta charset="utf-8">
<title>Kestrel Office Clearance – Business Card</title>
<link rel="stylesheet" href="https://fonts.googleapis.com/css2?family=Montserrat:wght@500;600;700&display=swap">
<style>
  :root {
    --backdrop: #e9ebee;
    --brand-blue: #1d5f92;
    --brand-blue-bright: #1b7bbc;
    --card-white: #ffffff;
    --text-white: #ffffff;
    --text-blue: #1c5d90;
  }
  * { box-sizing: border-box; margin: 0; padding: 0; }
  html, body {
    width: 1200px; height: 900px; overflow: hidden;
    background: var(--backdrop);
    font-family: "Montserrat", sans-serif;
  }
  .canvas { position: relative; width: 1200px; height: 900px; }

  .card {
    position: absolute;
    width: 640px; height: 370px;
    border-radius: 26px;
    overflow: hidden;
    box-shadow: 0 10px 28px rgba(0,0,0,.18);
  }

  /* Front */
  .card--front { left: 110px; top: 60px; background: var(--brand-blue); color: var(--text-white); }
  .front__flourish {
    position: absolute; left: 50px; top: 130px; width: 220px; height: 260px;
    border-radius: 50%;
    background: radial-gradient(closest-side, rgba(120,165,205,.38), rgba(120,165,205,.12) 60%, rgba(120,165,205,0));
  }
  .front__brand {
    position: absolute; left: 0; right: 0; top: 48px;
    display: flex; flex-direction: column; align-items: center; gap: 18px;
  }
  .front__mark { width: 118px; height: 118px; border-radius: 50%; background: var(--card-white); }
  .front__name { font-size: 22px; font-weight: 700; letter-spacing: .5px; text-transform: uppercase; }
  .front__tagline {
    position: absolute; left: 0; right: 0; top: 250px;
    text-align: center; font-size: 17px; font-weight: 600; letter-spacing: .4px;
    text-transform: uppercase;
  }
  .front__web {
    position: absolute; right: 40px; bottom: 36px;
    font-size: 14px; font-weight: 600; letter-spacing: .6px;
  }

  /* Back */
  .card--back { left: 450px; top: 470px; background: var(--card-white); }
  .back__band { position: absolute; left: 0; top: 0; width: 360px; height: 370px; }
  .back__band-label {
    position: absolute; left: 40px; top: 160px; width: 220px;
    color: var(--text-white); font-size: 30px; font-weight: 700; letter-spacing: 1px;
    text-transform: uppercase; text-align: center;
  }
  .back__details {
    position: absolute; right: 36px; top: 40px;
    text-align: right; color: var(--text-blue);
  }
  .back__person { font-size: 24px; font-weight: 700; text-transform: uppercase; line-height: 1.05; }
  .back__role { font-size: 13px; font-weight: 600; color: var(--brand-blue-bright); text-transform: uppercase; letter-spacing: .8px; margin-bottom: 12px; }
  .back__address { font-size: 14px; font-weight: 500; line-height: 1.45; margin-bottom: 12px; }
  .back__contact { list-style: none; font-size: 14px; font-weight: 600; line-height: 1.6; }
  .back__contact li { display: flex; align-items: center; justify-content: flex-end; gap: 8px; }
  .back__contact li.contact--phone { font-size: 16px; }
  .icon { width: 13px; height: 13px; flex: none; }
</style>
</head>
<body>
<main class="canvas">

  <section class="card card--front" aria-label="Business card front">
    <div class="front__flourish" role="img" aria-label="Faint flame-like flourish decoration"></div>
    <div class="front__brand">
      <div class="front__mark"></div>
      <h1 class="front__name">Kestrel Office Clearance</h1>
    </div>
    <p class="front__tagline">Office clearances at no cost... we take it all away</p>
    <p class="front__web">www.kestrelofficeclear.co.uk</p>
  </section>

  <section class="card card--back" aria-label="Business card back">
    <svg class="back__band" viewBox="0 0 360 370" aria-hidden="true">
      <circle cx="90" cy="250" r="270" fill="var(--brand-blue)"/>
    </svg>
    <p class="back__band-label">Kestrel</p>

    <div class="back__details">
      <h2 class="back__person">Mark Holloway</h2>
      <p class="back__role">Director</p>
      <p class="back__address">Unit K4 B, 3-7 Fenwick Lane,<br>Ashcombe,<br>Marlow Vale, ZX9 4QT</p>
      <ul class="back__contact">
        <li class="contact--phone">07700 913528
          <svg class="icon" viewBox="0 0 16 16"><rect x="4" y="1" width="8" height="14" rx="1.5" fill="none" stroke="currentColor" stroke-width="1.6"/><circle cx="8" cy="12.5" r=".9" fill="currentColor"/></svg>
        </li>
        <li class="contact--phone">01632 960418
          <svg class="icon" viewBox="0 0 16 16"><path d="M4 1.5 6 5 4.6 6.6a8 8 0 0 0 4.8 4.8L11 10l3.5 2-1 2.5C8 15 1 8 1.5 2.5z" fill="none" stroke="currentColor" stroke-width="1.4" stroke-linejoin="round"/></svg>
        </li>
        <li>mark@kestrelofficeclear.co.uk
          <svg class="icon" viewBox="0 0 16 16"><rect x="1" y="3" width="14" height="10" rx="1.5" fill="none" stroke="currentColor" stroke-width="1.5"/><path d="M1.5 4 8 9l6.5-5" fill="none" stroke="currentColor" stroke-width="1.5"/></svg>
        </li>
        <li>www.kestrelofficeclear.co.uk
          <svg class="icon" viewBox="0 0 16 16"><circle cx="8" cy="8" r="6.5" fill="none" stroke="currentColor" stroke-width="1.4"/><ellipse cx="8" cy="8" rx="2.8" ry="6.5" fill="none" stroke="currentColor" stroke-width="1.2"/><path d="M1.5 8h13" stroke="currentColor" stroke-width="1.2"/></svg>
        </li>
      </ul>
    </div>
  </section>

</main>
</body>
</html>
```